Post Card Design - For Financial

"9" length 6.5" height" post card of tallhedge.net trying to get people to text the word YES to our phone number to access our latest stock picks. or marketrove.io we own both of them. Call to action. Get winnin stock picks sign up now text the word "YES" to 888-312-4798. must haves: " track record 2023: 477.8%" "#1 stock picking newsletter in the U.S.A." " Disclaimer: The materials and content provided by TallHedge.net, including but not limited to our website, emails, blogs, and text messages (collectively, the "Materials"), are intended for general information purposes only and do not constitute financial, legal, or investment advice. TallHedge.net is engaged in the business of marketing and advertising companies for compensation. The information contained in the Materials is not, and should not be read as, an offer or recommendation to buy or sell any securities. All content is provided for informational and educational purposes only. TallHedge.net and its staff are not licensed investment advisors, brokers, or dealers. Any content provided by us is not intended to solicit or recommend any investment and should not be used as the basis for any investment decisions. We do not provide investment advice, endorse any financial product, or suggest that any particular investment or strategy is suitable for any specific person. TallHedge.net receives compensation from the companies featured in our alerts, emails, and other Materials for marketing and advertising services. The existence of such compensation may influence the content, topics, or posts made in the Materials. Investing in stocks, especially penny stocks, involves a high level of risk and may not be suitable for all investors. The possibility exists that you could sustain a loss of some or all of your initial investment. Therefore, you should not invest money that you cannot afford to lose. The performance figures stated in the Materials, including but not limited to a track record of 477% in 2023, are hypothetical and should not be considered indicative of future results. Past performance is not necessarily indicative of future results. Individual results may vary, and the examples used in the Materials are not guaranteed to occur. You are encouraged to perform your own due diligence and consult with a qualified financial advisor before making any investment decisions. TallHedge.net and its Materials should not be used as the sole basis for any investment decision. We make no representation or warranty as to the accuracy, completeness, or reliability of the information contained in the Materials. The content provided by TallHedge.net and in its newsletter is intended for entertainment purposes only. Acknowledgment: By using TallHedge.net's services, joining our site, or subscribing to our email/blog list, you acknowledge that you have read, understood, and agree to be bound by the terms of this disclaimer. If you do not agree with these terms, you should not use our services or subscribe to our Materials

."

Target Market(s)

investors

Industry/Entity Type

financial

Colors
0054AA
0677BA
7BADD7
CADEEF
E8F1F8
00AB8E
00BBA5
67D7C9
C6EFE9
E9F9F6
59FF00
82FF00
B8FF75
E3FFCB
F4FFEA

Requirements
Must have
• " track record 2023: 477.8%" "#1 stock picking newsletter in the U.S.A." "Disclaimer: The materials and content provided by TallHedge.net, including but not limited to our website, emails, blogs, and text messages (collectively, the "Materials"), are intended for general information purposes only and do not constitute financial, legal, or investment advice. TallHedge.net is engaged in the business of marketing and advertising companies for compensation. The information contained in the Materials is not, and should not be read as, an offer or recommendation to buy or sell any securities. All content is provided for informational and educational purposes only. TallHedge.net and its staff are not licensed investment advisors, brokers, or dealers. Any content provided by us is not intended to solicit or recommend any investment and should not be used as the basis for any investment decisions. We do not provide investment advice, endorse any financial product, or suggest that any particular investment or strategy is suitable for any specific person. TallHedge.net receives compensation from the companies featured in our alerts, emails, and other Materials for marketing and advertising services. The existence of such compensation may influence the content, topics, or posts made in the Materials. Investing in stocks, especially penny stocks, involves a high level of risk and may not be suitable for all investors. The possibility exists that you could sustain a loss of some or all of your initial investment. Therefore, you should not invest money that you cannot afford to lose. The performance figures stated in the Materials, including but not limited to a track record of 477% in 2023, are hypothetical and should not be considered indicative of future results. Past performance is not necessarily indicative of future results. Individual results may vary, and the examples used in the Materials are not guaranteed to occur. You are encouraged to perform your own due diligence and consult with a qualified financial advisor before making any investment decisions. TallHedge.net and its Materials should not be used as the sole basis for any investment decision. We make no representation or warranty as to the accuracy, completeness, or reliability of the information contained in the Materials. The content provided by TallHedge.net and in its newsletter is intended for entertainment purposes only. Acknowledgment: By using TallHedge.net's services, joining our site, or subscribing to our email/blog list, you acknowledge that you have read, understood, and agree to be bound by the terms of this disclaimer. If you do not agree with these terms, you should not use our services or subscribe to our Materials."
Nice to have
• call to action: Get exclusive stock picks delivered directly to your phone. Text "YES" to [888-312-4798] to receive your first stock pick

```html
<!DOCTYPE html>
<html lang="en">
<head>
<meta charset="UTF-8">
<title>TallHedge.net Postcard</title>
<link href="https://fonts.googleapis.com/css2?family=Poppins:ital,wght@0,400;0,500;0,600;1,700&family=Roboto+Condensed:wght@400;700&display=swap" rel="stylesheet">
<style>
  :root {
    --backdrop: #ececec;
    --card-white: #ffffff;
    --brand-blue: #1255a6;
    --accent-lime: #b4d433;
    --lime-fold: #8fab22;
    --ink-white: #ffffff;
    --ink-dark: #2a2f1a;
  }
  * { box-sizing: border-box; margin: 0; padding: 0; }
  html, body {
    width: 1200px;
    height: 900px;
    overflow: hidden;
    background: var(--backdrop);
  }
  .postcard {
    position: absolute;
    left: 45px;
    top: 49px;
    width: 1110px;
    height: 802px;
    background: var(--card-white);
    box-shadow: 0 2px 10px rgba(0,0,0,0.12);
  }
  .promo-panel {
    position: absolute;
    left: 0;
    top: 0;
    width: 548px;
    height: 802px;
    background: var(--brand-blue);
    color: var(--ink-white);
    font-family: "Poppins", sans-serif;
  }
  .headline {
    position: absolute;
    left: 46px;
    top: 44px;
    font-size: 35px;
    line-height: 1.2;
    font-weight: 400;
  }
  .headline em {
    font-style: italic;
    font-weight: 700;
  }
  .cta-label {
    position: absolute;
    left: 46px;
    top: 160px;
    font-size: 35px;
    font-weight: 400;
  }
  .cta-label strong {
    color: var(--accent-lime);
    font-weight: 600;
  }
  .phone-number {
    position: absolute;
    left: 44px;
    top: 204px;
    font-size: 55px;
    font-weight: 500;
    color: var(--accent-lime);
    letter-spacing: -0.5px;
  }
  .track-record {
    position: absolute;
    left: 46px;
    top: 356px;
    font-size: 35px;
    font-weight: 400;
    line-height: 1.2;
  }
  .track-record .figure {
    display: block;
    color: var(--accent-lime);
    font-weight: 600;
  }
  .disclaimer-band {
    position: absolute;
    left: 0;
    top: 480px;
    width: 576px;
    height: 255px;
    background: var(--accent-lime);
    padding: 28px 28px 0 38px;
  }
  .disclaimer-text {
    font-family: "Roboto Condensed", sans-serif;
    font-size: 8.1px;
    line-height: 1.31;
    color: var(--ink-dark);
    text-align: justify;
  }
  .disclaimer-text b { font-weight: 700; }
  .band-fold {
    position: absolute;
    left: 548px;
    top: 735px;
  }
</style>
</head>
<body>
  <div class="postcard">
    <section class="promo-panel">
      <h1 class="headline">Get <em>Winning</em> stock picks<br>sign up now!</h1>
      <p class="cta-label">Text "<strong>YES</strong>" To</p>
      <p class="phone-number">888-312-4798</p>
      <p class="track-record">Track Record 2023:<span class="figure">477.8%</span></p>
    </section>
    <div class="disclaimer-band">
      <p class="disclaimer-text"><b>Disclaimer:</b> The materials and content provided by TallHedge.net, including but not limited to our website, emails, blogs, and text messages (collectively, the "Materials"), are intended for general information purposes only and do not constitute financial, legal, or investment advice. TallHedge.net is engaged in the business of marketing and advertising companies for compensation. The information contained in the Materials is not, and should not be read as, an offer or recommendation to buy or sell any securities. All content is provided for informational and educational purposes only. TallHedge.net and its staff are not licensed investment advisors, brokers, or dealers. Any content provided by us is not intended to solicit or recommend any investment and should not be used as the basis for any investment decisions. We do not provide investment advice, endorse any financial product, or suggest that any particular investment or strategy is suitable for any specific person. TallHedge.net receives compensation from the companies featured in our alerts, emails, and other Materials for marketing and advertising services. The existence of such compensation may influence the content, topics, or posts made in the Materials. Investing in stocks, especially penny stocks, involves a high level of risk and may not be suitable for all investors. The possibility exists that you could sustain a loss of some or all of your initial investment. Therefore, you should not invest money that you cannot afford to lose. The performance figures stated in the Materials, including but not limited to a track record of 477% in 2023, are hypothetical and should not be considered indicative of future results. Past performance is not necessarily indicative of future results. Individual results may vary, and the examples used in the Materials are not guaranteed to occur. You are encouraged to perform your own due diligence and consult with a qualified financial advisor before making any investment decisions. TallHedge.net and its Materials should not be used as the sole basis for any investment decision. We make no representation or warranty as to the accuracy, completeness, or reliability of the information contained in the Materials. The content provided by TallHedge.net and in its newsletter is intended for entertainment purposes only. Acknowledgment: By using TallHedge.net's services, joining our site, or subscribing to our email/blog list, you acknowledge that you have read, understood, and agree to be bound by the terms of this disclaimer. If you do not agree with these terms, you should not use our services or subscribe to our Materials."</p>
    </div>
    <svg class="band-fold" width="28" height="17" viewBox="0 0 28 17" aria-hidden="true">
      <polygon points="0,0 28,0 0,17" fill="var(--lime-fold)"/>
    </svg>
  </div>
</body>
</html>
```